Pinegate Mobile Imaging
Mobile ultrasound business cards
Danelle Forbush Sonographer
Owner
418 Whitford Ave. Ste 203-117 Ashby Hollow, KY 40990
leave space to add later
danelle_forbush2006@mailbright.net
There is also a second owner that once design is finalized we will need to edit the text to put her information on the card.
email used on card will need to be changed at a later date!

```html
<!DOCTYPE html>
<html lang="en">
<head>
<meta charset="utf-8">
<title>Pinegate Mobile Imaging – Stationery Concepts</title>
<link href="https://fonts.googleapis.com/css2?family=Libre+Baskerville:wght@400;700&display=swap" rel="stylesheet">
<style>
  :root{
    --stage:#8e8f93;
    --paper:#ffffff;
    --ink:#1a1a1a;
    --muted:#6a6a6a;
    --plum:#7b2d8e;
    --plum-dark:#5a1d6b;
    --night:#141414;
    --night-soft:#2a2a2a;
    --fold:#c9c9c9;
  }
  *{box-sizing:border-box;margin:0;padding:0}
  html,body{width:1200px;height:458px;overflow:hidden;background:var(--stage)}
  body{font-family:"Libre Baskerville",Georgia,serif;color:var(--ink);position:relative}
  .piece{position:absolute;background:var(--paper);overflow:hidden}
  .wave{position:absolute;left:0;bottom:0;width:100%;display:block}

  /* brand name: one colour, one weight */
  .brand-name{position:absolute;color:var(--plum);font-weight:700;line-height:1;white-space:nowrap}
  .contact{position:absolute;color:var(--muted);line-height:1.6;white-space:nowrap}

  /* business cards */
  .card{left:31px;width:150px;height:84px}
  .card-front{top:108px}
  .card-back{top:216px;background:var(--night)}
  .card-plain{top:312px}
  .card-front .brand-name{left:9px;top:14px;font-size:11px}
  .card-front .contact{right:8px;top:11px;text-align:right;font-size:3.8px;color:var(--ink)}
  .card-front .contact strong{font-size:5px;color:var(--plum-dark)}
  .card-plain .brand-name{left:0;right:0;top:22px;text-align:center;font-size:15px}
  .card-plain .contact{left:0;right:0;top:42px;text-align:center;font-size:4.6px}

  /* letterheads */
  .letter{top:44px;width:240px;height:370px}
  .letter-a{left:200px}
  .letter-b{left:468px}
  .letter .brand-name{font-size:16px;top:16px}
  .letter-a .brand-name{left:16px}
  .letter-a .contact{right:14px;top:14px;text-align:right;font-size:3.8px}
  .letter-b .brand-name{left:0;right:0;text-align:center}
  .letter-b .contact{left:16px;top:42px;font-size:3.8px}

  /* envelopes */
  .envelope{left:830px;width:340px}
  .envelope svg.flap{position:absolute;inset:0;width:100%;height:100%}
  .env-plum{top:106px;height:64px;background:var(--plum)}
  .env-night{top:168px;height:58px;background:var(--night)}
  .env-white{top:226px;height:66px}

  /* compliment slip */
  .slip{left:768px;top:300px;width:256px;height:98px}
  .slip .brand-name{left:14px;top:14px;font-size:13px}
  .slip .contact{left:14px;top:32px;font-size:3.8px}

  .board-title{position:absolute;left:1040px;top:412px;font-size:12px;color:#f2f2f2;white-space:nowrap}
</style>
</head>
<body>

<!-- business cards -->
<div class="piece card card-front">
  <span class="brand-name">Pinegate</span>
  <div class="contact">
    <strong>Danelle Forbush</strong><br>
    Sonographer · Owner<br>
    418 Whitford Ave. Ste 203-117<br>
    Ashby Hollow, KY 40990<br>
    danelle_forbush2006@mailbright.net
  </div>
  <svg class="wave" viewBox="0 0 100 30" height="24" preserveAspectRatio="none" aria-hidden="true">
    <path d="M0 12 C30 30 60 0 100 10 L100 30 L0 30Z" fill="var(--plum)"/>
    <path d="M0 9 C30 27 60 -3 100 7" fill="none" stroke="var(--ink)" stroke-width="1.2" vector-effect="non-scaling-stroke"/>
  </svg>
</div>

<div class="piece card card-back"></div>

<div class="piece card card-plain">
  <span class="brand-name">Pinegate</span>
  <div class="contact">Pinegate Mobile Imaging</div>
  <svg class="wave" viewBox="0 0 100 30" height="18" preserveAspectRatio="none" aria-hidden="true">
    <path d="M0 14 C30 30 60 2 100 12 L100 30 L0 30Z" fill="var(--plum)"/>
    <path d="M0 11 C30 27 60 -1 100 9" fill="none" stroke="var(--ink)" stroke-width="1" vector-effect="non-scaling-stroke"/>
  </svg>
</div>

<!-- letterheads -->
<div class="piece letter letter-a">
  <span class="brand-name">Pinegate</span>
  <div class="contact">
    Pinegate Mobile Imaging<br>
    418 Whitford Ave. Ste 203-117<br>
    Ashby Hollow, KY 40990<br>
    danelle_forbush2006@mailbright.net
  </div>
  <svg class="wave" viewBox="0 0 100 30" height="56" preserveAspectRatio="none" aria-hidden="true">
    <path d="M0 12 C30 30 60 0 100 10 L100 30 L0 30Z" fill="var(--plum)"/>
    <path d="M0 9 C30 27 60 -3 100 7" fill="none" stroke="var(--ink)" stroke-width="1.5" vector-effect="non-scaling-stroke"/>
  </svg>
</div>

<div class="piece letter letter-b">
  <span class="brand-name">Pinegate</span>
  <div class="contact">
    Pinegate Mobile Imaging<br>
    418 Whitford Ave. Ste 203-117<br>
    Ashby Hollow, KY 40990<br>
    danelle_forbush2006@mailbright.net
  </div>
  <svg class="wave" viewBox="0 0 100 30" height="56" preserveAspectRatio="none" aria-hidden="true">
    <path d="M0 12 C30 30 60 0 100 10 L100 30 L0 30Z" fill="var(--plum)"/>
    <path d="M0 9 C30 27 60 -3 100 7" fill="none" stroke="var(--ink)" stroke-width="1.5" vector-effect="non-scaling-stroke"/>
  </svg>
</div>

<!-- envelopes -->
<div class="piece envelope env-plum">
  <svg class="flap" viewBox="0 0 340 64" preserveAspectRatio="none" aria-hidden="true">
    <path d="M0 0 L170 40 L340 0Z" fill="var(--plum-dark)"/>
  </svg>
</div>

<div class="piece envelope env-night">
  <svg class="flap" viewBox="0 0 340 58" preserveAspectRatio="none" aria-hidden="true">
    <path d="M0 0 L170 36 L340 0Z" fill="var(--night-soft)"/>
  </svg>
</div>

<div class="piece envelope env-white">
  <svg class="flap" viewBox="0 0 340 66" preserveAspectRatio="none" aria-hidden="true">
    <path d="M0 0 L170 40 L340 0" fill="none" stroke="var(--fold)" stroke-width="1"/>
  </svg>
</div>

<!-- compliment slip -->
<div class="piece slip">
  <span class="brand-name">Pinegate</span>
  <div class="contact">
    418 Whitford Ave. Ste 203-117<br>
    Ashby Hollow, KY 40990
  </div>
  <svg class="wave" viewBox="0 0 100 30" height="30" preserveAspectRatio="none" aria-hidden="true">
    <path d="M0 12 C30 30 60 0 100 10 L100 30 L0 30Z" fill="var(--plum)"/>
    <path d="M0 9 C30 27 60 -3 100 7" fill="none" stroke="var(--ink)" stroke-width="1.2" vector-effect="non-scaling-stroke"/>
  </svg>
</div>

<p class="board-title">Stationary Concepts</p>

</body>
</html>
```